Brochure for concert

I need a brochure design for the concert. Attached please find last year's brochure (Oveli Concert Programme.pdf).
The contents of this year's brochure can be found in the document 'Concert program.docx.'
The design of the brochure should be consistent with the invitation card.

```html
<!DOCTYPE html>
<html lang="en">
<head>
<meta charset="utf-8">
<title>Wildfern Debut Concert Invitation</title>
<link rel="stylesheet" href="https://fonts.googleapis.com/css2?family=Libre+Caslon+Text:wght@400;700&family=Great+Vibes&family=Oswald:wght@500&display=swap">
<style>
  :root {
    --page-bg: #e6e6e6;
    --ink-black: #050306;
    --plum-deep: #1e0a22;
    --plum-mid: #3a1238;
    --rose-glow: #7a2a5a;
    --gold-light: #f0d98a;
    --gold: #c9a540;
    --gold-dark: #9c7a22;
    --silver-light: #ffffff;
    --silver: #c8c8c8;
    --silver-dark: #8a8a8a;
    --text-white: #ffffff;
    --pill-text: #3a1238;
  }
  * { margin: 0; padding: 0; box-sizing: border-box; }
  html, body {
    width: 900px; height: 1200px; overflow: hidden;
    background: var(--page-bg);
  }
  .invitation {
    position: absolute;
    left: 25.5px; top: 0;
    width: 719px; height: 1016px;
    transform: scale(1.1811);
    transform-origin: 0 0;
    overflow: hidden;
    background:
      radial-gradient(ellipse 70% 35% at 70% 62%, rgba(122, 42, 90, 0.45), transparent 70%),
      linear-gradient(180deg, var(--ink-black) 0%, #12061a 28%, var(--plum-deep) 45%, var(--plum-mid) 68%, #1a0818 88%, var(--ink-black) 100%);
  }
  .backdrop-portrait {
    position: absolute; left: 0; top: 10px; width: 330px; height: 640px;
    background: radial-gradient(ellipse 55% 50% at 45% 40%, rgba(70, 40, 55, 0.55), transparent 75%);
  }
  .feature-photo {
    position: absolute; left: 0; top: 215px; width: 370px; height: 600px;
    background:
      radial-gradient(ellipse 40% 22% at 55% 22%, rgba(200, 160, 150, 0.55), transparent 80%),
      radial-gradient(ellipse 45% 45% at 50% 62%, rgba(210, 170, 175, 0.85), transparent 80%),
      linear-gradient(180deg, transparent 0%, rgba(160, 90, 120, 0.35) 40%, rgba(120, 40, 80, 0.55) 80%, transparent 100%);
  }
  .crowd-silhouette {
    position: absolute; left: 0; bottom: 0; width: 719px; height: 180px;
    background: linear-gradient(180deg, transparent 0%, rgba(60, 30, 50, 0.45) 50%, rgba(5, 3, 6, 0.85) 100%);
  }
  .band-label {
    position: absolute; right: 57px; top: 92px;
    font-family: "Libre Caslon Text", serif; font-size: 92px; line-height: 1;
    letter-spacing: 2px;
    background: linear-gradient(180deg, var(--silver-light) 0%, var(--silver) 55%, var(--silver-dark) 100%);
    -webkit-background-clip: text; background-clip: text; color: transparent;
  }
  .band-name {
    position: absolute; right: 57px; top: 192px;
    font-family: "Libre Caslon Text", serif; font-size: 74px; line-height: 1;
    background: linear-gradient(180deg, var(--gold-light) 0%, var(--gold) 50%, var(--gold-dark) 100%);
    -webkit-background-clip: text; background-clip: text; color: transparent;
  }
  .event-tagline {
    position: absolute; right: 57px; top: 283px;
    font-family: "Libre Caslon Text", serif; font-size: 28px; line-height: 1;
    color: var(--gold);
  }
  .performer-name {
    position: absolute; left: 250px; top: 318px;
    font-family: "Great Vibes", cursive; font-size: 170px; line-height: 1.1;
    background: linear-gradient(180deg, var(--silver-light) 0%, var(--silver) 60%, var(--silver-dark) 100%);
    -webkit-background-clip: text; background-clip: text; color: transparent;
  }
  .gold-pill {
    position: absolute; right: 0;
    border-radius: 28px 0 0 28px;
    background: linear-gradient(90deg, var(--gold-light) 0%, var(--gold) 55%, var(--gold-dark) 100%);
    display: flex; align-items: center; justify-content: center;
  }
  .join-pill { top: 530px; width: 329px; height: 55px; }
  .join-pill span {
    font-family: "Libre Caslon Text", serif; font-size: 33px; color: var(--pill-text);
  }
  .phone-pill { top: 801px; width: 352px; height: 52px; }
  .phone-pill span {
    font-family: "Oswald", sans-serif; font-weight: 500; font-size: 38px;
    color: var(--text-white); text-shadow: 1px 2px 3px rgba(0,0,0,0.55);
  }
  .event-details {
    position: absolute; right: 32px; top: 608px; text-align: right;
    font-family: "Libre Caslon Text", serif; color: var(--text-white);
  }
  .event-date { font-size: 29px; line-height: 1.2; }
  .event-time { font-size: 34px; line-height: 1.2; margin-right: 8px; }
  .event-address {
    position: absolute; right: 38px; top: 714px; text-align: right;
    font-family: "Libre Caslon Text", serif; font-size: 22px; line-height: 1.5;
    color: var(--text-white); font-style: normal;
  }
  .stream-link {
    position: absolute; left: 0; width: 719px; top: 924px; text-align: center;
    font-family: "Libre Caslon Text", serif; font-size: 19px; color: var(--text-white);
    letter-spacing: 0.5px;
  }
</style>
</head>
<body>
  <main class="invitation">
    <div class="backdrop-portrait" role="img" aria-label="Faint enlarged portrait of the young performer in the background"></div>
    <div class="crowd-silhouette" role="img" aria-label="Silhouettes of a concert crowd with music notes"></div>
    <div class="feature-photo" role="img" aria-label="Photo of the young performer in a pink gown holding lilies"></div>

    <h1 class="band-label">BAND</h1>
    <h2 class="band-name">WILDFERN</h2>
    <p class="event-tagline">debut concert featuring</p>
    <p class="performer-name">Oveli</p>

    <div class="gold-pill join-pill"><span>JOIN US</span></div>

    <div class="event-details">
      <p class="event-date">SATURDAY, AUGUST 21</p>
      <p class="event-time">7pm - 8pm</p>
    </div>

    <address class="event-address">48 linden court<br>maple grove, nj 08000</address>

    <div class="gold-pill phone-pill"><span>555 0142 7788</span></div>

    <p class="stream-link">Live StreamRoom Link: meet.streamroom.us/j</p>
  </main>
</body>
</html>
```